Sleek and elegant promotional banner/sign for The Vellinor Law Firm

We need a design for promotional items like banners, signs, print ads, etc. that includes our firm name - "The Vellinor Law Firm" - and what we do. We advise businesses and individuals on legal matters; we represent individuals and businesses in litigation and transactions; we select and create business entities; we solve legal problems for individuals and businesses, etc. PLEASE DO NOT SIMPLY REPEAT THE PREVIOUS SENTENCE ON THE DESIGN. Please create a tag-line or brief description from ours. We need something that describes what we do in concise and creative manner while communicating trust and confidence. The banner must also include our basic contact information: 948.512-7740 (telephone) and vellinorlaw.com (website). You may use one or more of the attached images, but needn't use any with the right design. The design should be sleek and modern.

Target Market(s)

wealthy individuals and small business owners, entrepreneurs

Industry/Entity Type

Lawyer

Font styles to use
Sans Serif

Colors
33a6d7
0556a4
33b8a4

Requirements
Must have
• Firm name, contact information, BRIEF description of our services, sleek and elegant.
• Also, the design must be horizontal - not vertical.
Nice to have
• I'd like to use one of the images
Should not have
• Cliches

```html
<!DOCTYPE html>
<html lang="en">
<head>
<meta charset="utf-8">
<title>The Vellinor Law Firm – Banner</title>
<link rel="stylesheet" href="https://fonts.googleapis.com/css2?family=Open+Sans:wght@600;700&family=Roboto+Condensed:wght@400;700&display=swap">
<style>
  :root {
    --sky: #33a6d7;
    --navy: #0556a4;
    --teal: #33b8a4;
    --bright: #1d95e6;
    --white: #ffffff;
    --stage: #e6e6e6;
    --puzzle-light: #9cc8e8;
    --puzzle-mid: #6aa8d6;
  }
  html, body {
    margin: 0;
    width: 1200px;
    height: 1200px;
    overflow: hidden;
    background: var(--stage);
  }
  .banner {
    position: absolute;
    left: 108px;
    top: 405px;
    width: 985px;
    height: 395px;
    overflow: hidden;
    color: var(--white);
  }
  .banner-shapes { position: absolute; inset: 0; }
  .firm-name {
    position: absolute;
    left: 0; width: 474px;
    top: 28px;
    margin: 0;
    text-align: center;
    font: 700 49px/1 "Open Sans", sans-serif;
    letter-spacing: 0.5px;
  }
  .firm-sub {
    position: absolute;
    left: 0; width: 474px;
    top: 88px;
    text-align: center;
    font: 700 26px/1 "Open Sans", sans-serif;
    letter-spacing: 0.5px;
  }
  .tagline {
    position: absolute;
    left: 0; width: 474px;
    top: 140px;
    margin: 0;
    text-align: center;
    font-family: "Roboto Condensed", sans-serif;
    text-transform: uppercase;
  }
  .tagline-lead {
    display: block;
    font-weight: 700;
    font-size: 84px;
    line-height: 84px;
  }
  .tagline-rest {
    display: block;
    font-weight: 400;
    font-size: 45px;
    line-height: 44px;
  }
  .website {
    position: absolute;
    left: 55px;
    top: 343px;
    font: 700 36px/40px "Open Sans", sans-serif;
    letter-spacing: 0.5px;
  }
  .phone-icon {
    position: absolute;
    left: 520px;
    top: 333px;
    width: 48px;
    height: 48px;
  }
  .phone {
    position: absolute;
    left: 587px;
    top: 326px;
    font: 700 57px/62px "Open Sans", sans-serif;
  }
</style>
</head>
<body>
<section class="banner">
  <svg class="banner-shapes" width="985" height="395" viewBox="0 0 985 395" xmlns="http://www.w3.org/2000/svg">
    <defs>
      <linearGradient id="puzzleTone" x1="0" y1="0" x2="1" y2="1">
        <stop offset="0" stop-color="var(--puzzle-light)"/>
        <stop offset="1" stop-color="var(--puzzle-mid)"/>
      </linearGradient>
      <radialGradient id="panelGlow" cx="0.5" cy="0.5" r="0.65">
        <stop offset="0" stop-color="var(--bright)"/>
        <stop offset="1" stop-color="var(--navy)"/>
      </radialGradient>
      <linearGradient id="phoneBand" x1="0" y1="0" x2="1" y2="0">
        <stop offset="0" stop-color="var(--navy)"/>
        <stop offset="0.55" stop-color="#10a2ee"/>
        <stop offset="1" stop-color="var(--navy)"/>
      </linearGradient>
      <linearGradient id="rule" x1="0" y1="0" x2="1" y2="0">
        <stop offset="0" stop-color="var(--teal)" stop-opacity="0"/>
        <stop offset="0.5" stop-color="var(--teal)"/>
        <stop offset="1" stop-color="var(--teal)" stop-opacity="0"/>
      </linearGradient>
    </defs>
    <rect class="puzzle-photo" width="985" height="395" fill="url(#puzzleTone)" role="img" aria-label="Photo of light blue jigsaw puzzle pieces arranged in concentric rings"/>
    <polygon class="brand-panel" points="0,0 537,0 485,395 0,395" fill="url(#panelGlow)"/>
    <rect class="name-rule" x="25" y="101" width="425" height="3" fill="url(#rule)"/>
    <polygon class="web-band" points="0,333 492,333 480,393 0,393" fill="var(--teal)"/>
    <polygon class="phone-band" points="502,313 985,313 985,393 488,393" fill="url(#phoneBand)" stroke="var(--white)" stroke-width="2"/>
  </svg>

  <h1 class="firm-name">THE VELLINOR</h1>
  <div class="firm-sub">LAW FIRM</div>

  <p class="tagline">
    <span class="tagline-lead">We Solve</span>
    <span class="tagline-rest">The Most Puzzling</span>
    <span class="tagline-rest">Legal Problems</span>
  </p>

  <div class="website">www.vellinorlaw.com</div>

  <svg class="phone-icon" viewBox="0 0 48 48" xmlns="http://www.w3.org/2000/svg" aria-hidden="true">
    <circle cx="24" cy="24" r="21" fill="none" stroke="var(--white)" stroke-width="2.5"/>
    <path d="M16 14c1-1 2.5-1 3.2 0l2.3 3.4c.6.9.4 2-.4 2.7l-1.4 1.2c1.2 2.6 3.2 4.6 5.8 5.8l1.2-1.4c.7-.8 1.8-1 2.7-.4l3.4 2.3c1 .7 1 2.2 0 3.2l-1.4 1.4c-1.4 1.4-3.6 1.7-5.4.8C20.8 30.6 17.4 27.2 15 22c-.9-1.8-.6-4 .8-5.4z" fill="var(--white)"/>
    <path d="M26 13a9 9 0 0 1 9 9M26 17a5 5 0 0 1 5 5" fill="none" stroke="var(--white)" stroke-width="2" stroke-linecap="round"/>
  </svg>
  <div class="phone">948.512-7740</div>
</section>
</body>
</html>
```